Clearway Lending Template Design

We need a corporate letterhead template (word) and slide show template (PowerPoint) designed for our Motor Vehicle finance business.

Clearway Lending provides motor vehicle finance to the credit impaired. Please feel free to visit our website www.clearwaylending-example.com

Both templates (word and PowerPoint) must include the Clearway logo (attached to this project) and can be very similar in design.

We are after something creative yet professional in design.

Please feel free to ask any questions.

Thank you
Marisol

```html
<!DOCTYPE html>
<html lang="en">
<head>
<meta charset="utf-8">
<title>Clearway Lending Stationery</title>
<link rel="stylesheet" href="https://fonts.googleapis.com/css2?family=Arimo:wght@400;700&family=Questrial&display=swap">
<style>
  :root {
    --backdrop: #e8e8e8;
    --paper: #f7f7f7;
    --brand-green: #2e9e3a;
    --brand-green-light: #43bd4a;
    --brand-grey: #6e6e6e;
    --brand-grey-light: #a9a9a9;
    --ink: #5a5a5a;
    --rule: #9a9a9a;
    --cell-fill: #e2e2e2;
  }
  * { box-sizing: border-box; margin: 0; padding: 0; }
  html, body { width: 1200px; height: 815px; overflow: hidden; }
  body { background: var(--backdrop); position: relative; font-family: "Questrial", sans-serif; }

  .sheet {
    position: absolute; top: 72px; width: 482px; height: 683px;
    background: var(--paper); box-shadow: 0 2px 6px rgba(0,0,0,0.12);
  }
  .sheet--letterhead { left: 80px; }
  .sheet--fax { left: 638px; }

  .brand {
    position: absolute; left: 45px; top: 50px;
    display: flex; align-items: center; gap: 10px;
  }
  .brand__square { width: 38px; height: 38px; background: var(--brand-grey); }
  .brand__name { font-family: "Questrial", sans-serif; font-size: 19px; color: var(--brand-green); letter-spacing: 0.3px; }

  .footer-contact {
    position: absolute; left: 41px; top: 644px;
    font-size: 6.6px; line-height: 9px; color: var(--ink);
  }
  .footer-contact b { color: var(--brand-green); font-weight: 400; }

  .footer-band { position: absolute; left: 0; bottom: 0; width: 482px; height: 12px; }

  .fax-title {
    position: absolute; right: 42px; top: 40px;
    font-family: "Arimo", sans-serif; font-size: 64px; color: var(--ink); letter-spacing: 1px;
  }

  .fax-details {
    position: absolute; left: 41px; top: 139px; width: 397px;
    border-collapse: collapse; font-family: "Arimo", sans-serif; font-size: 7px; color: #444;
  }
  .fax-details td { border: 1px solid var(--rule); height: 14.6px; padding: 0 4px; font-weight: 700; }
  .fax-details .label { width: 42px; }
  .fax-details .value { width: 156px; }

  .fax-body {
    position: absolute; left: 40px; top: 227px; width: 398px; height: 387px;
    border: 1px solid var(--rule);
  }
  .fax-flags { display: flex; height: 15px; border-bottom: 1px solid var(--rule); background: var(--cell-fill); }
  .fax-flags span {
    flex: 1; display: flex; align-items: center; justify-content: center; gap: 3px;
    font-family: "Arimo", sans-serif; font-size: 7px; font-weight: 700; color: #444;
    border-right: 1px solid var(--rule);
  }
  .fax-flags span:last-child { border-right: none; }
  .fax-flags i { width: 5px; height: 5px; border: 1px solid #777; display: inline-block; }
  .fax-comments-label {
    text-align: center; margin-top: 11px;
    font-family: "Arimo", sans-serif; font-size: 7px; color: #444;
  }
</style>
</head>
<body>

<section class="sheet sheet--letterhead">
  <div class="brand"><span class="brand__square"></span><span class="brand__name">Clearway Lending</span></div>
  <p class="footer-contact">Unit 7 Harrowfield Trade Park, Meadowbank Lane, London<br>
    <b>T:</b> 0700 410 410 · <b>F:</b> 0700 410 411 · <b>E:</b> info@clearwaylending-example.com</p>
  <svg class="footer-band" viewBox="0 0 482 12" preserveAspectRatio="none" aria-hidden="true">
    <defs>
      <linearGradient id="greyBandA" x1="0" x2="1"><stop offset="0" stop-color="#555"/><stop offset="1" stop-color="#bbb"/></linearGradient>
      <linearGradient id="greenBandA" x1="0" x2="1"><stop offset="0" stop-color="#43bd4a"/><stop offset="1" stop-color="#2e9e3a"/></linearGradient>
    </defs>
    <polygon points="0,7 283,7 279,12 0,12" fill="url(#greyBandA)"/>
    <polygon points="290,0 482,0 482,12 279,12" fill="url(#greenBandA)"/>
  </svg>
</section>

<section class="sheet sheet--fax">
  <div class="brand"><span class="brand__square"></span><span class="brand__name">Clearway Lending</span></div>
  <h1 class="fax-title">FAX</h1>

  <table class="fax-details">
    <tr><td class="label">To:</td><td class="value"></td><td class="label">From:</td><td class="value"></td></tr>
    <tr><td class="label">Fax:</td><td class="value"></td><td class="label">Pages:</td><td class="value"></td></tr>
    <tr><td class="label">Phone:</td><td class="value"></td><td class="label">Date:</td><td class="value"></td></tr>
    <tr><td class="label">Re:</td><td class="value"></td><td class="label">CC:</td><td class="value"></td></tr>
  </table>

  <div class="fax-body">
    <div class="fax-flags">
      <span><i></i>Urgent</span>
      <span><i></i>For Review</span>
      <span><i></i>Please Comment</span>
      <span><i></i>Please Reply</span>
      <span><i></i>Please Recycle</span>
    </div>
    <p class="fax-comments-label">COMMENTS:</p>
  </div>

  <p class="footer-contact">Unit 7 Harrowfield Trade Park, Meadowbank Lane, London<br>
    <b>T:</b> 0700 410 410 · <b>F:</b> 0700 410 411 · <b>E:</b> info@clearwaylending-example.com</p>
  <svg class="footer-band" viewBox="0 0 482 12" preserveAspectRatio="none" aria-hidden="true">
    <defs>
      <linearGradient id="greyBandB" x1="0" x2="1"><stop offset="0" stop-color="#555"/><stop offset="1" stop-color="#bbb"/></linearGradient>
      <linearGradient id="greenBandB" x1="0" x2="1"><stop offset="0" stop-color="#43bd4a"/><stop offset="1" stop-color="#2e9e3a"/></linearGradient>
    </defs>
    <polygon points="0,7 283,7 279,12 0,12" fill="url(#greyBandB)"/>
    <polygon points="290,0 482,0 482,12 279,12" fill="url(#greenBandB)"/>
  </svg>
</section>

</body>
</html>
```